Business card

would like a double sided business card made up with my logos provided.
Prefer card to have black background and to use the black logos, with matching blue writing for the text.
One side to just be the logo, (Try to use both the black logos)
the other side to have the logo and also my credentials/business information.

Covering all aspects of Carpentry and Building Services

Marcus Tolvey
Qualified Carpenter
Mob: 0417263948
Email: rkt.joinery@mailbright.com
ABN: 47 615 209 834

Industry/Entity Type

Business

Contact Information for Business Card

Marcus Tolvey
Qualified Carpenter
Mob: 0417263948
ABN: 47 615 209 834

Requirements
Must have
• Please try to use both the black logos and incorporate into the card.

```html
<!DOCTYPE html>
<html lang="en">
<head>
<meta charset="utf-8">
<title>RKT Joinery – Business Card</title>
<link href="https://fonts.googleapis.com/css2?family=Montserrat:wght@300;400;600;800&display=swap" rel="stylesheet">
<style>
  :root {
    --bg: #e9e6e1;
    --card: #0e0f10;
    --card-edge: #1c1e20;
    --band: #17191b;
    --white: #f4f5f6;
    --blue: #1fa3dc;
    --grey: #c9cbcd;
  }
  * { margin: 0; padding: 0; box-sizing: border-box; }
  html, body { width: 1200px; height: 885px; overflow: hidden; }
  body {
    background: var(--bg);
    font-family: "Montserrat", Arial, sans-serif;
    display: flex;
    flex-direction: column;
    align-items: center;
    justify-content: center;
    gap: 56px;
  }
  .card {
    position: relative;
    width: 640px;
    height: 366px;
    border-radius: 22px;
    background: radial-gradient(ellipse at 40% 40%, var(--card-edge) 0%, var(--card) 70%);
    box-shadow: 0 10px 30px rgba(0,0,0,.25);
    overflow: hidden;
    color: var(--white);
  }
  /* brand lockup */
  .brand { display: flex; align-items: center; gap: 14px; }
  .brand-mark { width: 22px; height: 22px; background: var(--blue); }
  .brand-name { font-weight: 800; letter-spacing: 1px; color: var(--white); line-height: 1; }
  .brand-tagline {
    color: var(--blue); font-weight: 400; text-transform: uppercase;
    letter-spacing: 6px; font-size: 13px; margin-top: 10px;
  }

  /* details side */
  .card--details .divider-band {
    position: absolute; top: 0; bottom: 0; left: 420px; width: 78px;
    background: var(--band);
    border-left: 1px solid #2a2d30; border-right: 1px solid #2a2d30;
  }
  .card--details .brand-block { position: absolute; left: 44px; top: 46px; }
  .card--details .brand-name { font-size: 40px; }
  .card--details .person { position: absolute; left: 150px; top: 150px; text-align: center; width: 260px; }
  .person-name { font-size: 26px; font-weight: 600; }
  .person-title { color: var(--blue); font-size: 16px; margin-top: 4px; }
  .contact {
    position: absolute; left: 110px; top: 236px; width: 340px;
    text-align: center; font-size: 17px; line-height: 1.6; font-weight: 400;
  }
  .contact .abn { color: var(--blue); }

  /* logo side */
  .card--logo .brand-block { position: absolute; right: 56px; top: 86px; text-align: left; }
  .card--logo .brand-mark { width: 34px; height: 34px; }
  .card--logo .brand-name { font-size: 64px; }
  .card--logo .brand-tagline { font-size: 15px; letter-spacing: 7px; margin-top: 14px; }
  .card--logo .services {
    position: absolute; left: 48px; bottom: 40px;
    font-size: 17px; color: var(--white); font-weight: 400;
  }
</style>
</head>
<body>

  <section class="card card--details" aria-label="Business card, details side">
    <div class="divider-band"></div>
    <div class="brand-block">
      <div class="brand">
        <span class="brand-mark"></span>
        <span class="brand-name">RKT JOINERY</span>
      </div>
      <p class="brand-tagline">Carpenters and Builders</p>
    </div>
    <div class="person">
      <p class="person-name">Marcus Tolvey</p>
      <p class="person-title">Qualified Carpenter</p>
    </div>
    <div class="contact">
      <p class="phone">0417263948</p>
      <p class="email">rkt.joinery@mailbright.com</p>
      <p class="abn">ABN: 47 615 209 834</p>
    </div>
  </section>

  <section class="card card--logo" aria-label="Business card, logo side">
    <div class="brand-block">
      <div class="brand">
        <span class="brand-mark"></span>
        <span class="brand-name">RKT JOINERY</span>
      </div>
      <p class="brand-tagline">Carpenters and Builders</p>
    </div>
    <p class="services">all aspects of Carpentry and Building Services</p>
  </section>

</body>
</html>
```